Website for Corvalind Capital, my new firm that raises money from investors to buy, build, own an...

Corvalind Capital needs a website! We are a new company with very experienced people, who invest in, own and build hotel properties, as well as apartments and other commercial real estate. We seek investors for our projects, and we provide safe, secure returns on their investment in our projects. Our new logo is designed to exhibit strength, class and security, and would like our website to continue on this theme. Our name, Corvalind, is a word-play on a Greek word “aristeia”, which means “excellence” and “a warriors finest moment of glory in war”. If you are in business, you realize that much of it is like war, with strategy and moves and opponents and competitors, and ever-changing economic conditions and threats that make business very much like war. We like to think that we are good at business (war), and so have named our company “Corvalind”, using the founders last name and the word “aristeia” combined. Another definition of "aristeia" is "performing at the peak of one's potential after a long struggle"...again, much like business in real life! The website design should exhibit financial security, smart moves, and positive growth towards a bright future.

Target Market(s)

The target market is smart and wealthy investors, with others such as brokers, cities and government agencies, lenders, sellers, partners, etc also looking at it.

Industry/Entity Type

Investment

Number of Pages Required

5+ page

Font styles to use
Sans Serif

Colors
fec214

Requirements
Must have
• Our website should have a landing page, a "about" or bio page, a projects page and a contact us page. Our new logo uses the colors black and gold, so this should be factored in to our site. The site should be simple, yet impactful and impressive. I have actually two logos, which can be mixed and interchanged in a complimentary way, each with their own unique look.
Nice to have
• I have uploaded a couple screenshots of a website i like, and the simplicity I mention.
Should not have
• The site should not be flashy or complicated or complex or "busy"

```html
<!DOCTYPE html>
<html lang="en">
<head>
<meta charset="utf-8">
<title>Corvalind Capital</title>
<link href="https://fonts.googleapis.com/css2?family=Marcellus&family=Libre+Baskerville:wght@400;700&family=Montserrat:ital,wght@0,400;0,600;1,600;1,700&display=swap" rel="stylesheet">
<style>
:root{
  --gold:#c9962e;
  --gold-soft:#d6a640;
  --ink:#2b2b2b;
  --dark:#262626;
  --white:#ffffff;
  --muted:#6b6b6b;
  --green:#3cb64a;
}
*{margin:0;padding:0;box-sizing:border-box}
html,body{width:1200px;height:1200px;overflow:hidden;background:var(--white)}
body{position:relative;font-family:'Libre Baskerville',serif;color:var(--ink)}
.abs{position:absolute}
.brand{left:150px;top:6px;display:flex;align-items:center;gap:6px;font-family:'Marcellus',serif;font-size:15px;letter-spacing:2px;color:var(--ink)}
.brand-mark{width:10px;height:10px;background:var(--gold)}
.nav{left:150px;top:38px;width:854px;height:24px;border-bottom:3px solid var(--gold);display:flex}
.nav a{flex:1;text-align:center;font-family:'Marcellus',serif;font-size:11px;color:var(--ink);text-decoration:none;line-height:30px;border-right:4px solid var(--gold)}
.nav a:first-child{flex:0.8}
.hero{left:0;top:74px;width:1200px;height:162px;background:linear-gradient(90deg,#d9d2c2 0%,#cdb99c 45%,#b7865a 70%,#9e5c35 100%)}
.hero h1{position:absolute;left:264px;top:0;font-family:'Marcellus',serif;font-weight:400;font-size:33px;line-height:27px;color:var(--white);letter-spacing:1px}
.hero p{position:absolute;left:258px;top:62px;width:756px;font-size:8.4px;line-height:14px;font-weight:700;color:var(--white)}
.btn-join{position:absolute;left:540px;top:144px;width:70px;height:12px;background:var(--gold);color:var(--white);font-size:7px;font-weight:700;text-align:center;line-height:12px}
.title{font-family:'Marcellus',serif;font-size:18px;color:var(--gold);text-align:center;width:1200px;left:0}
.photo{position:absolute}
.about-text{left:664px;top:270px;width:382px;font-size:8.6px;line-height:9.9px}
.band{left:0;width:1200px;background:var(--dark)}
.card-text{width:258px;font-size:6.4px;line-height:8.2px;font-weight:700;color:var(--white)}
.btn-out{height:27px;border:3px solid var(--gold);font-family:'Marcellus',serif;font-size:11px;text-align:center;line-height:21px}
.band .btn-out{color:var(--white)}
.stat-text{left:608px;top:712px;width:392px;font-family:'Montserrat',sans-serif;font-size:7.4px;line-height:7.4px;letter-spacing:.6px;color:var(--ink)}
.step{width:70px;height:28px;border-radius:50%;background:var(--gold);font-family:'Marcellus',serif;font-size:20px;text-align:center;line-height:28px;color:var(--ink)}
.step-text{width:340px;font-size:5.2px;line-height:8.5px;font-weight:700;color:var(--white)}
.quote-bar{left:532px;top:1019px;width:518px;height:8px;background:var(--gold)}
.quote-box{left:488px;top:1027px;width:562px;height:73px;background:var(--dark)}
.quote-text{left:548px;top:1036px;width:412px;font-family:'Montserrat',sans-serif;font-size:8.6px;line-height:7.4px;letter-spacing:.3px;color:var(--white)}
.dot{width:18px;height:8px;border-radius:50%;top:1104px;background:var(--gold)}
.dot.on{background:#222}
.footer{left:0;top:1132px;width:1200px;height:68px;background:var(--dark);font-family:'Montserrat',sans-serif;color:var(--white)}
.footer h4{position:absolute;font-style:italic;font-weight:600;font-size:11px;letter-spacing:.8px}
.f-line{position:absolute;font-size:8.2px;font-weight:600;letter-spacing:.8px;display:flex;align-items:center;gap:8px}
.f-menu{position:absolute;left:410px;top:16px;font-size:7.6px;font-style:italic;font-weight:700;line-height:9px;letter-spacing:.5px}
.f-social{position:absolute;font-size:6.4px;font-style:italic;font-weight:700;letter-spacing:.6px}
.f-icon{position:absolute;width:16px;height:16px;border-radius:50%;background:var(--white)}
.email{left:712px;top:20px;width:239px;height:19px;background:var(--white);color:var(--muted);font-size:6px;font-style:italic;padding-left:10px;line-height:22px;position:absolute}
.subscribe{left:960px;top:20px;width:79px;height:19px;background:var(--gold);font-size:6px;font-weight:700;text-align:center;line-height:19px;position:absolute}
.legal{position:absolute;top:61px;font-size:5px;font-weight:600}
</style>
</head>
<body>

<div class="abs brand"><span class="brand-mark"></span>CORVALIND</div>

<nav class="abs nav">
  <a>Home</a><a>Portfolio</a><a>What We Do</a><a>About Us</a><a>Careers</a><a style="border-right-width:4px">Contact</a>
</nav>

<section class="abs hero" role="img" aria-label="Photo of high-rise apartment towers under a pale sky with a plane passing">
  <h1>Social Impact + Venture Capital=<br>Social Impact Capital</h1>
  <p>Lorem ipsum dolor sit amet, consectetur adipiscing elit, sed do eiusmod tempor incididunt ut labore et dolore magna aliqua. Ut enim ad minim veniam, quis nostrud exercitation ullamco laboris nisi ut aliquip ex ea commodo consequat. Duis aute irure dolor in reprehenderit in voluptate velit esse cillum dolore eu fugiat nulla pariatur. Excepteur sint occaecat cupidatat non proident, sunt in culpa qui officia deserunt mollit anim id est laborum. Sed ut perspiciatis unde omnis iste natus error sit voluptatem accusantium doloremque laudantium, totam rem aperiam, eaque ipsa quae ab illo inventore veritatis et quasi architecto beatae vitae dicta sunt explicabo. Nemo enim ipsam</p>
  <div class="btn-join">Join Now</div>
</section>

<h2 class="abs title" style="top:242px">About Us</h2>
<div class="photo" style="left:150px;top:265px;width:484px;height:147px;background:linear-gradient(180deg,#d8c3a8 0%,#c9a680 40%,#4f6a3a 70%,#5fb4c6 100%)" role="img" aria-label="Hotel courtyard with palm trees and a swimming pool"></div>
<p class="abs about-text">Lorem ipsum dolor sit amet, consectetur adipiscing elit, sed do eiusmod tempor incididunt ut labore et dolore magna aliqua. Ut enim ad minim veniam, quis nostrud exercitation ullamco laboris nisi ut aliquip ex ea commodo consequat. Duis aute irure dolor in reprehenderit in voluptate velit esse cillum dolore eu fugiat nulla pariatur. Excepteur sint occaecat cupidatat non proident, sunt in culpa qui officia deserunt mollit anim id est laborum. Sed ut perspiciatis unde omnis iste natus error sit voluptatem accusantium doloremque laudantium, totam rem aperiam, eaque ipsa quae ab illo inventore veritatis et quasi architecto beatae vitae dicta sunt explicabo. Nemo enim ipsam voluptatem quia voluptas sit aspernatur aut odit aut fugit, sed quia consequuntur magni dolores eos qui ratione voluptatem sequi nesciunt. Neque porro quisquam est, qui dolorem ipsum quia dolor sit amet, consectetur, adipisci</p>

<section class="abs band" style="top:445px;height:203px">
  <h2 class="abs title" style="top:0">Portfolio</h2>
  <div class="photo" style="left:143px;top:29px;width:288px;height:102px;background:linear-gradient(160deg,#1f3a3c,#51646a 50%,#2a3335)" role="img" aria-label="Aerial view of twin skyscrapers at dusk"></div>
  <div class="photo" style="left:450px;top:29px;width:288px;height:102px;background:linear-gradient(180deg,#c9b3c4 0%,#b596a6 55%,#6a4a55 100%)" role="img" aria-label="City skyline with a tall tower at sunset"></div>
  <div class="photo" style="left:754px;top:29px;width:288px;height:102px;background:linear-gradient(90deg,#3b4c5a,#8fa4b4 50%,#2d3a44)" role="img" aria-label="Glass office towers seen from above"></div>
  <p class="abs card-text" style="left:157px;top:135px">Lorem ipsum dolor sit amet, consectetur adipiscing elit, sed do eiusmod tempor incididunt ut labore et dolore magna aliqua. Ut enim ad minim veniam, quis nostrud exercitation ullamco laboris nisi ut aliquip ex</p>
  <p class="abs card-text" style="left:463px;top:135px">Lorem ipsum dolor sit amet, consectetur adipiscing elit, sed do eiusmod tempor incididunt ut labore et dolore magna aliqua. Ut enim ad minim veniam, quis nostrud exercitation ullamco laboris nisi ut aliquip ex</p>
  <p class="abs card-text" style="left:768px;top:135px">Lorem ipsum dolor sit amet, consectetur adipiscing elit, sed do eiusmod tempor incididunt ut labore et dolore magna aliqua. Ut enim ad minim veniam, quis nostrud exercitation ullamco laboris nisi ut aliquip ex</p>
  <div class="abs btn-out" style="left:216px;top:172px;width:128px">More Info</div>
  <div class="abs btn-out" style="left:523px;top:172px;width:128px">More Info</div>
  <div class="abs btn-out" style="left:824px;top:172px;width:128px">More Info</div>
</section>

<h2 class="abs title" style="top:669px">Our Monthly Statement</h2>
<svg class="abs" style="left:150px;top:686px" width="450" height="154" viewBox="150 686 450 154" font-family="Montserrat, sans-serif">
  <text x="418" y="698" font-size="9" fill="#2b2b2b" letter-spacing=".5">Monthly Income Stats</text>
  <text x="418" y="704" font-size="4.5" fill="#999">Current year</text>
  <text x="418" y="710" font-size="4.5" fill="#999">Last year</text>
  <circle cx="556" cy="701" r="2.4" fill="#c9962e"/>
  <g stroke="#e2e2e2" stroke-width=".6">
    <line x1="170" y1="723" x2="566" y2="723"/><line x1="170" y1="734" x2="566" y2="734"/>
    <line x1="170" y1="745" x2="566" y2="745"/><line x1="170" y1="757" x2="566" y2="757"/>
    <line x1="170" y1="768" x2="566" y2="768"/><line x1="170" y1="779" x2="566" y2="779"/>
    <line x1="170" y1="790" x2="566" y2="790"/><line x1="170" y1="802" x2="566" y2="802"/>
    <line x1="170" y1="813" x2="566" y2="813"/>
    <line x1="210" y1="712" x2="210" y2="826"/><line x1="250" y1="712" x2="250" y2="826"/>
    <line x1="290" y1="712" x2="290" y2="826"/><line x1="330" y1="712" x2="330" y2="826"/>
    <line x1="370" y1="712" x2="370" y2="826"/><line x1="410" y1="712" x2="410" y2="826"/>
    <line x1="450" y1="712" x2="450" y2="826"/><line x1="490" y1="712" x2="490" y2="826"/>
    <line x1="530" y1="712" x2="530" y2="826"/>
  </g>
  <rect x="170" y="712" width="396" height="114" fill="none" stroke="#2b2b2b" stroke-width="1.4"/>
  <g font-size="7.5" fill="#2b2b2b" text-anchor="end">
    <text x="165" y="715">11</text><text x="165" y="726">10</text><text x="165" y="737">9</text>
    <text x="165" y="748">8</text><text x="165" y="760">7</text><text x="165" y="771">6</text>
    <text x="165" y="782">5</text><text x="165" y="793">4</text><text x="165" y="805">3</text>
    <text x="165" y="816">2</text><text x="165" y="827">1</text>
  </g>
  <g font-size="8" fill="#2b2b2b" text-anchor="middle" letter-spacing=".6">
    <text x="188" y="837">Jan</text><text x="233" y="837">Feb</text><text x="276" y="837">Apr</text>
    <text x="322" y="837">May</text><text x="364" y="837">Jun</text><text x="405" y="837">Jul</text>
    <text x="454" y="837">Aug</text><text x="496" y="837">Sep</text><text x="539" y="837">Oct</text>
    <text x="585" y="837">Nov</text>
  </g>
  <polyline points="170,798 194,787 270,778 328,766 390,779 408,756 440,742 509,714" fill="none" stroke="#c9962e" stroke-width="4" stroke-linejoin="round"/>
  <g fill="#2b2b2b"><circle cx="194" cy="787" r="2.6"/><circle cx="328" cy="766" r="2.6"/><circle cx="390" cy="779" r="2.6"/><circle cx="408" cy="756" r="2.6"/><circle cx="509" cy="714" r="2.6"/></g>
  <rect x="374" y="738" width="64" height="9" rx="4.5" fill="#3cb64a" stroke="#2b2b2b" stroke-width=".6"/>
  <path d="M402 747 L406 751 L410 747Z" fill="#3cb64a"/>
  <text x="403" y="745" font-size="6" fill="#ffffff" text-anchor="middle">$7.3</text>
</svg>
<p class="abs stat-text">Lorem ipsum dolor sit amet, consectetur adipiscing elit, sed do eiusmod tempor incididunt ut labore et dolore magna aliqua. Ut enim ad minim veniam, quis nostrud exercitation ullamco laboris nisi ut aliquip ex ea commodo consequat. Duis aute irure dolor in reprehenderit in voluptate velit esse cillum dolore eu fugiat nulla pariatur. Excepteur sint occaecat cupidatat non proident, sunt in culpa qui officia deserunt mollit anim id est laborum. Sed ut perspiciatis unde omnis iste natus error sit voluptatem accusantium doloremque laudantium, totam rem aperiam, eaque ipsa quae ab illo inventore veritatis et quasi architecto beatae vitae dicta sunt explicabo. Nemo enim ipsam voluptatem quia voluptas sit aspernatur aut odit aut fugit, sed quia consequuntur magni dolores eos qui ratione voluptatem sequi nesciunt. Neque porro quisquam est, qui dolorem ipsum quia dolor sit amet, consectetur, adipisci velit, sed quia non numquam eius modi tempora incidunt ut labore et dolore magnam aliquam quaerat voluptatem.</p>
<div class="abs btn-out" style="left:748px;top:805px;width:108px;height:25px;line-height:19px;font-size:9px">More Info</div>

<section class="abs band" style="top:852px;height:112px">
  <h2 class="abs title" style="top:4px">How It Works</h2>
  <div class="abs step" style="left:156px;top:32px">1</div>
  <p class="abs step-text" style="left:242px;top:34px">Lorem ipsum dolor sit amet, consectetur adipiscing elit, sed do eiusmod tempor incididunt ut labore et dolore magna aliqua. Ut enim ad minim veniam, quis nostrud exercitation ullamco laboris nisi ut aliquip ex ea commodo consequat. Duis aute irure dolor in reprehenderit in voluptate velit esse cillum dolore eu fugiat nulla pariatur. Excepteur sint occaecat cupidatat non proident, sunt in culpa qui officia deserunt mollit anim id est laborum. Sed ut perspiciatis unde omnis iste natus error sit voluptatem accusantium doloremque laudantium, totam rem aperiam, eaque ipsa quae ab illo inventore veritatis et quasi architecto beatae vitae dicta sunt explicabo. Nemo enim ipsam voluptatem quia voluptas sit aspernatur aut odit aut fugit, sed</p>
  <div class="abs step" style="left:612px;top:32px">2</div>
  <p class="abs step-text" style="left:698px;top:34px">Lorem ipsum dolor sit amet, consectetur adipiscing elit, sed do eiusmod tempor incididunt ut labore et dolore magna aliqua. Ut enim ad minim veniam, quis nostrud exercitation ullamco laboris nisi ut aliquip ex ea commodo consequat. Duis aute irure dolor in reprehenderit in voluptate velit esse cillum dolore eu fugiat nulla pariatur. Excepteur sint occaecat cupidatat non proident, sunt in culpa qui officia deserunt mollit anim id est laborum. Sed ut perspiciatis unde omnis iste natus error sit voluptatem accusantium doloremque laudantium, totam rem aperiam, eaque ipsa quae ab illo inventore veritatis et quasi architecto beatae vitae dicta sunt explicabo. Nemo enim ipsam voluptatem quia voluptas sit aspernatur aut odit aut fugit, sed</p>
</section>

<h2 class="abs title" style="top:979px">Clients Testimonial</h2>
<div class="abs quote-bar"></div>
<div class="abs quote-box"></div>
<div class="photo" style="left:150px;top:1007px;width:382px;height:83px;background:linear-gradient(90deg,#c9c2b5 0%,#a27e63 45%,#8a8478 100%)" role="img" aria-label="Portrait photo of a smiling client"></div>
<p class="abs quote-text">Lorem ipsum dolor sit amet, consectetur adipiscing elit, sed do eiusmod tempor incididunt ut labore et dolore magna aliqua. Ut enim ad minim veniam, quis nostrud exercitation ullamco laboris nisi ut aliquip ex ea commodo consequat. Duis aute irure dolor in reprehenderit in voluptate velit esse cillum dolore eu fugiat nulla pariatur. Excepteur sint occaecat cupidatat non proident, sunt in culpa qui officia deserunt mollit anim id est laborum. Sed ut perspiciatis unde omnis iste natus error sit</p>
<div class="abs dot" style="left:685px"></div>
<div class="abs dot on" style="left:716px"></div>
<div class="abs dot" style="left:746px"></div>

<footer class="abs footer">
  <h4 style="left:216px;top:2px">Contact Us</h4>
  <div class="f-line" style="left:175px;top:15px">
    <svg width="18" height="11" viewBox="0 0 18 11"><path d="M1 4 L9 0 L17 4Z M2 5 H16 V6 H2Z M3 6 V9 M6 6 V9 M9 6 V9 M12 6 V9 M15 6 V9 M1 10 H17" fill="#fff" stroke="#fff" stroke-width="1"/></svg>
    <span>Adress:418 Halden Ave</span>
  </div>
  <div class="f-line" style="left:177px;top:28px">
    <svg width="16" height="10" viewBox="0 0 16 10"><rect x=".5" y=".5" width="15" height="9" fill="none" stroke="#fff"/><path d="M.5 .5 L8 6 L15.5 .5" fill="none" stroke="#fff"/></svg>
    <span>Email:info@corvalind.example</span>
  </div>
  <div class="f-line" style="left:177px;top:40px">
    <svg width="16" height="11" viewBox="0 0 16 11"><path d="M2 1 Q0 3 3 7 Q7 11 10 10 L11 8 L8 6 L7 7 Q4 5 4 3 L5 2 L3 0Z" fill="#fff"/></svg>
    <span>Phone:555-014-2270</span>
  </div>
  <h4 style="left:410px;top:2px">Menu</h4>
  <div class="f-menu">About<br>Community<br>Resources<br>Services<br>Citie</div>
  <h4 style="left:545px;top:2px">Connect With Us</h4>
  <div class="f-icon" style="left:552px;top:14px"></div>
  <div class="f-icon" style="left:552px;top:32px"></div>
  <div class="f-icon" style="left:552px;top:49px"></div>
  <div class="f-social" style="left:592px;top:19px">Snapwell</div>
  <div class="f-social" style="left:600px;top:36px">Chirplane</div>
  <div class="f-social" style="left:592px;top:53px">Friendsy</div>
  <div class="email">Email</div>
  <div class="subscribe">Subscribe</div>
  <div class="legal" style="left:502px">Site Terms</div>
  <div class="legal" style="left:574px">State Disclosures</div>
  <div class="legal" style="left:672px">Help</div>
</footer>

</body>
</html>
```